Design an attractive wine label for Brell Fine Wines

we need a wine label design, we are an Australian wine exporting company'Brell Fine Wines'. We succeed several pallets in last few months and is going to launch our first container. So it’s time to start our own brands. we will have some wines display in China's shopping mall shelves, so we want to have a catchy label which can attract Chinese eyes immediately. other details you will see in the file i uploaded. The design should include a front and back label.

Target Market(s)

Brell Fine Wines are targeting middle class wine drinkers in 2nd-4th tier Chinese cities.

Colors

Designer to choose colors to be used in the design.

Requirements
Must have
• We’d like something that at first glance is Australian (element, style or color…) but subconsciously connects to the Chinese. Demeanor bearing in mind the demographics targeted across the ranges. We would expect the designs and naming to becoming more formalized as they rise to platinum.
Nice to have
• creative things come out
Should not have
• any dead related word or icon, no number '4' related word or icon, no skull related word or icon, kangaroo (see brand 'Copper vine')

```html
<!DOCTYPE html>
<html lang="en">
<head>
<meta charset="utf-8">
<title>Warrabee Cabernet Sauvignon – Front Label</title>
<link rel="stylesheet" href="https://fonts.googleapis.com/css2?family=Great+Vibes&family=Cormorant+Garamond:wght@500;600&display=swap">
<style>
  :root {
    --canvas: #a3a3a3;
    --label-black: #151515;
    --label-black-edge: #262626;
    --wine-red: #8a0a12;
    --wine-red-deep: #6a040b;
    --gold: #d9bf8c;
    --gold-light: #f1e2bf;
    --gold-dark: #a8844c;
    --ochre: #e0772f;
    --cream: #f3ead8;
  }
  * { margin: 0; padding: 0; box-sizing: border-box; }
  html, body {
    width: 1200px; height: 1200px; overflow: hidden;
    background: var(--canvas);
  }
  .canvas {
    position: relative; width: 1200px; height: 1200px;
    background: radial-gradient(ellipse at 50% 45%, #b0b0b0 0%, var(--canvas) 70%);
  }
  .front-label {
    position: absolute; left: 250px; top: 84px;
    width: 700px; height: 1032px;
    box-shadow: 0 18px 40px rgba(0,0,0,0.25);
  }
  .label-art { position: absolute; inset: 0; width: 100%; height: 100%; }
  .brand-name {
    position: absolute; left: 0; right: 0; top: 80px;
    text-align: center;
    font-family: "Great Vibes", cursive;
    font-size: 128px; line-height: 1;
    color: var(--gold);
  }
  .varietal {
    position: absolute; left: 0; right: 0; top: 768px;
    text-align: center;
    font-family: "Cormorant Garamond", serif;
    font-weight: 600; font-variant: small-caps;
    font-size: 46px; letter-spacing: 1px;
    color: var(--cream);
  }
  .vintage {
    position: absolute; left: 0; right: 0; top: 838px;
    display: flex; align-items: center; justify-content: center; gap: 22px;
    font-family: "Cormorant Garamond", serif;
    font-weight: 500; font-size: 40px; letter-spacing: 5px;
    color: var(--cream);
  }
  .vintage .rule { width: 78px; height: 2px; background: var(--cream); }
  .origin {
    position: absolute; left: 0; right: 0; top: 935px;
    text-align: center;
    font-family: "Great Vibes", cursive;
    font-size: 54px; color: var(--gold);
  }
</style>
</head>
<body>
<main class="canvas">
  <section class="front-label" aria-label="Warrabee Cabernet Sauvignon front label">
    <svg class="label-art" viewBox="0 0 700 1032" aria-hidden="false">
      <defs>
        <linearGradient id="blackPanel" x1="0" y1="0" x2="0" y2="1">
          <stop offset="0" stop-color="#1d1d1d"/>
          <stop offset="1" stop-color="#111"/>
        </linearGradient>
        <linearGradient id="redPanel" x1="0" y1="0" x2="0" y2="1">
          <stop offset="0" stop-color="#9a0c15"/>
          <stop offset="1" stop-color="#6e040b"/>
        </linearGradient>
        <linearGradient id="goldRibbon" x1="0" y1="0" x2="1" y2="0">
          <stop offset="0" stop-color="#a8844c"/>
          <stop offset="0.5" stop-color="#f1e2bf"/>
          <stop offset="1" stop-color="#b8955a"/>
        </linearGradient>
        <linearGradient id="patternBand" x1="0" y1="1" x2="1" y2="0">
          <stop offset="0" stop-color="#7a2a10"/>
          <stop offset="0.35" stop-color="#e0772f"/>
          <stop offset="0.7" stop-color="#c4452a"/>
          <stop offset="1" stop-color="#e9a05a"/>
        </linearGradient>
        <radialGradient id="medallion" cx="0.4" cy="0.35" r="0.7">
          <stop offset="0" stop-color="#f7ecd2"/>
          <stop offset="0.6" stop-color="#d9bf8c"/>
          <stop offset="1" stop-color="#a8844c"/>
        </radialGradient>
      </defs>

      <rect class="panel-black" x="0" y="0" width="700" height="1032" fill="url(#blackPanel)"/>

      <!-- lower red field rising in an arch -->
      <path class="panel-red" d="M0 740 Q300 300 700 470 L700 1032 L0 1032 Z" fill="url(#redPanel)"/>

      <!-- decorated arch band -->
      <path class="arch-pattern" role="img" aria-label="Dot-painting pattern band in ochre, orange and red"
            d="M0 650 Q280 160 700 250 L700 470 Q300 300 0 740 Z" fill="url(#patternBand)"/>

      <!-- gold ribbon edges -->
      <path class="arch-ribbon" d="M0 630 Q280 140 700 230 L700 255 Q280 170 0 656 Z" fill="url(#goldRibbon)"/>
      <path class="arch-edge" d="M0 742 Q300 302 700 472" fill="none" stroke="#1a1a1a" stroke-width="6"/>

      <!-- emblem medallion -->
      <circle class="emblem" role="img" aria-label="Koala emblem medallion"
              cx="350" cy="445" r="142" fill="url(#medallion)" stroke="#8f6d3a" stroke-width="4"/>
    </svg>

    <h1 class="brand-name">Warrabee</h1>
    <p class="varietal">Cabernet Sauvignon</p>
    <p class="vintage"><span class="rule"></span>2008<span class="rule"></span></p>
    <p class="origin">Australia</p>
  </section>
</main>
</body>
</html>
```